Roll-up Banner für Wolkenwerkstatt
Zielgruppe
Wir, die Norddeutscher Verband für Heitere Seelenkunde, widmen uns der Aus- und Fortbildung im Bereich der Positiven Psychologie. Wir bilden Coaches, Trainer, Berater, Therapeuten, Pädagogen und Führungskräfte darin aus, wie sie Ihren Klienten helfen können ein erfüllteres und glücklicheres Leben zu gestalten.
Wir arbeiten zusammen mit verschiedenen Universitäten, Forschern und Wissenschaftlern und ermöglichen so den Brückenschlag zwischen Wissenschaft und der praktischen Arbeit mit Klienten.
Wir zeichnen uns durch die Kombination von hoher Professionalität und großer menschlicher Wärme und Verbundenheit aus.
Unser Ziel ist es durch Wissensvermittlung einen gesellschaftlichen Unterschied zu machen. Der Mensch steht für uns im Mittelpunkt.
Unsere Zielgruppe sind Coaches, Trainer, Berater, Therapeuten, Pädagogen und Führungskräfte.
Aufgabenstellung
Das Banner soll als Rollup-Banner (1x2m) fungieren und uns bei Kongressen und Tagungen repräsentieren. Es muss von weitem gut erkennbar sein. Unser Logo sollte in irgendeiner Form enthalten sein eventuell auch nur Teile als grafische Einbindung. Der Firmenname Norddeutscher Verband für Heitere Seelenkunde, muss gut erkennbar sein. Die website nvhs-portal.example sollte gut sichtbar Teil des Entwurfes sein.
Bei der Einbindung von Bildern sollten Sie beachten, dass wir eine sehr heterogene Zielgruppe haben, sich also Pädagogen ebenso wiederfinden müssen wie Führungskräfte, Männer, wie Frauen. Ansonsten könnte auch eine grafische Lösung oder Bilder ohne Personen genutzt werden.
Wir haben Ihnen einige Beispiele für andere Werbematerialien von uns angehangen. Es wäre wichtig, dass das Banner zu diesem Corporate Design passt.
HINWEIS: Da wir das Banner bereits Ende nächster Woche einsetzen wollen, küren wir bereits am Montagmorgen (den 17.9.2018) den Sieger.

```html
<!DOCTYPE html>
<html lang="de">
<head>
<meta charset="utf-8">
<title>Roll-up Banner – Norddeutscher Verband für Heitere Seelenkunde</title>
<link href="https://fonts.googleapis.com/css2?family=Fira+Sans:wght@400;500;700&family=Crimson+Text:wght@400;700&display=swap" rel="stylesheet">
<style>
  :root {
    --green: #6cb84e;
    --mint: #17ad86;
    --teal: #00b2c4;
    --navy: #1c3b6e;
    --rule-navy: #14396a;
    --board: #2d2d2d;
    --board-light: #3c3c3c;
    --white: #ffffff;
    --ink: #2f3a45;
  }
  * { margin: 0; padding: 0; box-sizing: border-box; }
  html, body { width: 1200px; height: 2400px; overflow: hidden; background: var(--white); }
  .banner { position: relative; width: 1200px; height: 2400px; font-family: "Fira Sans", sans-serif; color: var(--white); }

  .header { position: absolute; left: 0; top: 0; width: 1200px; height: 382px; background: var(--white); }
  .header__band { position: absolute; inset: 0; }
  .brand { position: absolute; left: 146px; top: 236px; color: var(--navy); }
  .brand__short { display: flex; align-items: center; gap: 14px; font-size: 46px; font-weight: 700; letter-spacing: 4px; }
  .brand__dot { width: 22px; height: 22px; border-radius: 50%; background: var(--navy); }
  .brand__name { margin-top: 12px; font-size: 18px; line-height: 24px; font-weight: 500; width: 260px; }
  .website { position: absolute; left: 486px; top: 166px; width: 690px; font-size: 58px; line-height: 70px; font-weight: 700; letter-spacing: -1px; white-space: nowrap; }

  .visual { position: absolute; left: 0; top: 382px; width: 1200px; height: 638px;
    background: radial-gradient(ellipse at 50% 45%, var(--board-light), var(--board) 75%); }

  .info { position: absolute; left: 0; top: 1020px; width: 1200px; height: 1050px;
    background: linear-gradient(90deg, var(--green) 0%, var(--mint) 45%, var(--teal) 100%); }
  .intro { position: absolute; left: 66px; top: 84px; width: 356px; text-align: right; font-size: 21.5px; line-height: 30.6px; font-weight: 400; }
  .intro p + p { margin-top: 30px; }
  .intro strong { font-weight: 700; }
  .divider { position: absolute; left: 454px; top: 58px; width: 2px; height: 896px; background: var(--white); }
  .headline { position: absolute; left: 486px; top: 80px; font-size: 60px; line-height: 76px; font-weight: 700; white-space: nowrap; }
  .quote { position: absolute; left: 486px; top: 330px; width: 660px; font-family: "Crimson Text", serif; }
  .quote__mark { display: block; font-size: 200px; line-height: 1; font-weight: 700; margin-left: 262px; height: 90px; }
  .quote__text { font-size: 63px; line-height: 76px; margin-top: 30px; }
  .quote__footer { display: flex; align-items: center; margin-top: 24px; margin-left: 262px; height: 80px; }
  .quote__mark--close { font-size: 200px; line-height: 1; font-weight: 700; height: 80px; margin-top: 80px; }
  .quote__author { font-family: "Fira Sans", sans-serif; font-style: normal; font-size: 22px; font-weight: 700; margin-left: 36px; }

  .base-rule { position: absolute; left: 0; top: 2070px; width: 1200px; height: 7px; background: var(--rule-navy); }

  .partners { position: absolute; left: 0; top: 2077px; width: 1200px; height: 323px; background: var(--white); color: var(--navy); }
  .partners__title { position: absolute; left: 426px; top: 42px; font-size: 22px; font-weight: 400; }
  .partner { position: absolute; top: 130px; display: flex; align-items: center; gap: 10px; font-size: 18px; line-height: 22px; font-weight: 500; color: var(--ink); }
  .partner__mark { flex: none; width: 26px; height: 26px; border-radius: 50%; background: var(--navy); }
  .partner--1 { left: 58px; width: 190px; }
  .partner--2 { left: 286px; width: 230px; }
  .partner--3 { left: 590px; width: 270px; }
  .partner--4 { left: 930px; width: 240px; }
</style>
</head>
<body>
<div class="banner">
  <header class="header">
    <svg class="header__band" width="1200" height="382" viewBox="0 0 1200 382" aria-hidden="true">
      <defs>
        <linearGradient id="bandGradient" x1="0" y1="0" x2="1" y2="0">
          <stop offset="0" stop-color="#6cb84e"/>
          <stop offset="0.45" stop-color="#1fae80"/>
          <stop offset="1" stop-color="#00b2c4"/>
        </linearGradient>
      </defs>
      <polygon points="384,0 1200,0 1200,382 446,382" fill="url(#bandGradient)"/>
    </svg>
    <div class="brand">
      <div class="brand__short"><span class="brand__dot"></span>NVHS</div>
      <div class="brand__name">Norddeutscher Verband für Heitere Seelenkunde</div>
    </div>
    <div class="website">NVHS-PORTAL.EXAMPLE</div>
  </header>

  <div class="visual" role="img" aria-label="Kreidetafel mit einem traurigen und einem lächelnden Kreidegesicht, verbunden durch einen gelben Pfeil, den eine Hand mit Kreide zeichnet"></div>

  <section class="info">
    <div class="intro">
      <p>Wir, die <strong>Norddeutscher Verband für Heitere Seelenkunde</strong>, widmen uns der <strong>Aus- und Fortbildung</strong> im Bereich der Positiven Psychologie. Wir bilden Coaches, Trainer, Berater, Therapeuten, Pädagogen und Führungskräfte darin aus, wie sie Ihren Klienten helfen können ein erfüllteres und glücklicheres Leben zu gestalten.</p>
      <p>Wir arbeiten zusammen mit verschiedenen Universitäten, Forschern und Wissenschaftlern und ermöglichen so den Brückenschlag zwischen Wissenschaft und der praktischen Arbeit mit Klienten.</p>
      <p>Unser Ziel ist es durch Wissensvermittlung einen gesellschaftlichen Unterschied zu machen. Der Mensch steht für uns im Mittelpunkt.</p>
    </div>
    <div class="divider"></div>
    <h1 class="headline">Zertifizierte Ausbildung<br>Positive Bildung</h1>
    <blockquote class="quote">
      <span class="quote__mark">&#8221;</span>
      <p class="quote__text">Wenn wir anderen zum Glück verhelfen, werden wir selbst glücklich.</p>
      <footer class="quote__footer">
        <span class="quote__mark--close">&#8220;</span>
        <cite class="quote__author">HENRIK SOLBERG</cite>
      </footer>
    </blockquote>
  </section>

  <div class="base-rule"></div>

  <footer class="partners">
    <h2 class="partners__title">Forschungskooperationspartner:</h2>
    <div class="partner partner--1"><span class="partner__mark"></span>Hochschule Havelland</div>
    <div class="partner partner--2"><span class="partner__mark"></span>Akademie am Spreebogen</div>
    <div class="partner partner--3"><span class="partner__mark"></span>Universität Lindenau</div>
    <div class="partner partner--4"><span class="partner__mark"></span>Technische Hochschule Bergstraße</div>
  </footer>
</div>
</body>
</html>
```